KRV Business Cards

We are a local commercial development company based in Silicon Valley and we would like a new business card. I've attached a copy of our company brochure to give a flavor of what we do, our logo, info company colors/graphics, and our current business card. We don't necessarily need a crazy makeover, but would like something that feels a little bit more "fresh" and modern (we've had the same business card design for 15+ years), but still in keeping with our overall brand -- clean, high-quality, modern but timeless. Would like to add our website to the info on the card (www.velmara.com) and would like the flexibility for some folks to have an efax number listed and some not to have that included (without it looking like there is a hole).

```html
<!DOCTYPE html>
<html lang="en">
<head>
<meta charset="utf-8">
<title>KRV Business Cards</title>
<link href="https://fonts.googleapis.com/css2?family=Cinzel:wght@400&family=EB+Garamond:ital,wght@0,400;1,400&display=swap" rel="stylesheet">
<style>
  :root {
    --stage: #000000;
    --brand-blue: #38556d;
    --paper: #ffffff;
    --ink: #1c1c1c;
    --on-blue: #ffffff;
    --display: "Cinzel", serif;
    --text: "EB Garamond", serif;
  }
  * { margin: 0; padding: 0; box-sizing: border-box; }
  html, body { width: 1200px; height: 960px; overflow: hidden; background: var(--stage); }
  .canvas { position: relative; width: 1200px; height: 960px; }

  .card { position: absolute; top: 317px; width: 544px; height: 326px; overflow: hidden; }

  /* Contact side */
  .card-front { left: 36px; background: var(--paper); }
  .front-band { position: absolute; left: 0; top: 0; width: 100%; height: 163px; background: var(--brand-blue); }
  .front-company {
    position: absolute; left: 47px; top: 46px;
    font-family: var(--display); font-weight: 400; font-size: 29px; line-height: 30px;
    color: var(--on-blue); text-transform: uppercase; letter-spacing: 0.3px;
  }
  .holder { position: absolute; right: 46px; top: 166px; text-align: right; color: var(--ink); }
  .holder-name { font-family: var(--display); font-size: 20px; line-height: 22px; letter-spacing: 0.6px; text-transform: uppercase; }
  .holder-title { font-family: var(--text); font-style: italic; font-size: 17px; line-height: 15px; }

  .contact { position: absolute; left: 46px; right: 45px; color: var(--ink); font-family: var(--text); }
  .contact-address { top: 226px; font-size: 17.5px; line-height: 20px; letter-spacing: 2.3px; white-space: nowrap; text-align: justify; text-align-last: justify; }
  .contact-row { display: flex; justify-content: space-between; font-size: 16px; line-height: 18px; white-space: nowrap; }
  .contact-phones { top: 258px; }
  .contact-web { top: 284px; }
  .contact-row em { font-style: italic; }

  /* Brand side */
  .card-back { left: 621px; background: var(--brand-blue); color: var(--on-blue); }
  .back-frame { position: absolute; left: 37px; top: 35px; width: 469px; height: 255px; border: 1px solid var(--on-blue); }
  .back-company {
    position: absolute; left: 0; right: 0; top: 50px; text-align: center;
    font-family: var(--display); font-weight: 400; font-size: 45px; line-height: 46px; text-transform: uppercase;
  }
  .back-rule { position: absolute; left: 127px; top: 202px; width: 290px; border-top: 1px dotted var(--on-blue); opacity: 0.85; }
  .tagline {
    position: absolute; left: 0; right: 0; top: 218px; text-align: center;
    font-family: var(--text); font-style: italic; font-size: 22px; line-height: 27px;
  }
</style>
</head>
<body>
<div class="canvas">

  <section class="card card-front" aria-label="Business card, contact side">
    <div class="front-band"></div>
    <h1 class="front-company">Velmara<br>Land<br>Partners</h1>
    <div class="holder">
      <p class="holder-name">Hanna J. Lorimer</p>
      <p class="holder-title">Partner</p>
    </div>
    <p class="contact contact-address">218 Linden Street, Palo Alto, California 94301</p>
    <p class="contact contact-row contact-phones">
      <span><em>direct</em> 650.555.0142</span>
      <span><em>main</em> 650.555.0100</span>
      <span><em>fax</em> 650.555.0197</span>
    </p>
    <p class="contact contact-row contact-web">
      <span><em>email</em> hanna@velmara.com</span>
      <span>www.velmara.com</span>
    </p>
  </section>

  <section class="card card-back" aria-label="Business card, brand side">
    <div class="back-frame"></div>
    <h2 class="back-company">Velmara<br>Land<br>Partners</h2>
    <div class="back-rule"></div>
    <p class="tagline">Building Places<br>Made to Endure</p>
  </section>

</div>
</body>
</html>
```